Creating the leading Brochure Design Project

I would like a brochure thats going to help me sell my services to customers. It needs to really showcase we are more than just a sign company. We also handle lighting, electrical, graphics, car wraps. Led retro fit's , maintenance programs.

About

TVK Signs is a full service company for commercial electrical & signage needs and is committed to going above and beyond our customer’s expectations. Our mission is to provide exceptionally qualified services to all of our customers while staying competitive with our pricing.

Quality

Our primary mission is to bestow quality services at reasonable prices. TVK Signs is constantly striving to be on the cutting edge, providing the high quality service and attention to detail your project deserves. We have found that in every project, it’s all in the details!

Dependable

Our customers need reliable and dependable service with the assurance of knowing that the job will be completed on schedule. They continue returning for our Highest-quality services delivered on a timely manner by trustworthy, professional electricians at affordable prices.
Affordable

TVK Signs offers very affordable products and services that align with your business needs and budget. Providing quality, honest & dependable service doesn’t always need to come with an extravagant price tag. We look forward to providing you with a very competitive bid!

Target Market(s)

Bringing in new business

Industry/Entity Type

Digital Signage

Font styles to use
Serif

Colors
0255a3
f37529
9d9d9d
c3c3c3

Requirements
Must have
• I want to show our services along with WHY they need a LED Message center sign.
• Also want to inform them on the advantages of upgrading their current signs or building lighting / exterior lighting to LED.
• Tvk Signs - Designs, manufactures, installs, and services signs throughout the tri-state area of PA. We also offer LED signage, LED message center signs and LED lighting interior and exterior. Looking to have a fact page of why converting to LED lighting for your business and signage is the right idea. Also wanted to incorporate how important it is to have an LED message center sign. My blog on my website has some facts about LED's (tvksigns-example.net) Also you can pull photos off my site to incorporate into the brochure.
• LED signs are often the most cost-effective form of advertisement—especially for small business owners.The National Merchant Trade Bureau says that “Signs are the most effective, yet least expensive, form of advertising for the small business.”And that’s because small business owners using displays often see an increase in business between 15 and 150%. No other form of advertisement—from newspapers to radio to the Internet—offers the potential ROI of a solid LED sign.
Nice to have
• What’s the first thing that prospective customers see when they approach your business? Your signage tells them where you are, draws their attention and attracts them into your business (or possibly drives them away). Summing up your business brand for the world to see, your business signage creates that all-important first impression. How can you ensure it’s a good one? That's easy turn to TVK signs to help you develop the best signage your business needs.
• Once your sign is up, spend the time and money to maintain it. Replace burned-out bulbs promptly and keep it clean. Nothing turns prospective customers off like a broken or partially burned-out sign. It tells people you don’t care—and when they see that, they won’t care to do business with you.

```html
<!DOCTYPE html>
<html lang="en">
<head>
<meta charset="utf-8">
<title>Facts about LED displays</title>
<link rel="stylesheet" href="https://fonts.googleapis.com/css2?family=Oswald:wght@300;400&family=Open+Sans:wght@400;700;800&display=swap">
<style>
  :root {
    --navy: #27287f;
    --navy-glow: #3a3aa6;
    --title-blue: #5b5bad;
    --orange: #f37529;
    --white: #ffffff;
    --ink: #1b1b1b;
    --heading-blue: #2e2c86;
    --stage: #ececec;
  }
  * { box-sizing: border-box; margin: 0; padding: 0; }
  html, body {
    width: 1200px; height: 880px; overflow: hidden;
    background: var(--stage);
  }
  .spread {
    position: absolute; left: 69px; top: 30px;
    width: 1066px; height: 822px;
    display: flex;
    box-shadow: 0 2px 8px rgba(0,0,0,.25);
  }
  .facts-panel {
    position: relative; width: 702px; height: 100%;
    background: radial-gradient(ellipse 60% 55% at 52% 42%, var(--navy-glow), var(--navy) 70%);
    color: var(--white);
    font-family: "Open Sans", Arial, sans-serif;
  }
  .facts-title {
    position: absolute; left: 41px; top: 76px;
    font-family: "Oswald", "Arial Narrow", sans-serif;
    font-weight: 400; font-size: 70px; line-height: 1;
    color: var(--title-blue); letter-spacing: -0.5px; white-space: nowrap;
  }
  .fact-icon {
    position: absolute; width: 67px; height: 67px;
    border-radius: 50%; background: var(--orange);
    display: flex; align-items: center; justify-content: center;
  }
  .fact-text {
    position: absolute; font-size: 11px; line-height: 12.9px;
  }
  .fact-text strong { color: var(--orange); font-weight: 800; }
  .fact-photo {
    position: absolute; left: 407px; top: 604px; width: 250px; height: 141px;
    background: linear-gradient(160deg, #d9dde2 0%, #b8bfc7 35%, #9b2a2e 60%, #6c7178 100%);
  }
  .clients-panel {
    width: 364px; height: 100%; background: var(--white);
    padding: 45px 38px 0 45px;
    font-family: "Open Sans", Arial, sans-serif; color: var(--ink);
    font-size: 11px; line-height: 12.9px;
  }
  .clients-heading {
    font-family: "Oswald", "Arial Narrow", sans-serif; font-weight: 400;
    font-size: 20px; line-height: 26px; color: var(--heading-blue);
    margin-bottom: 10px; white-space: nowrap;
  }
  .clients-panel p { margin-bottom: 12.9px; }
  .price-line {
    font-family: "Oswald", "Arial Narrow", sans-serif; font-weight: 400;
    font-size: 20px; line-height: 27px; white-space: nowrap;
  }
  .price-neon { color: var(--heading-blue); margin-top: 6px; }
  .price-led { color: var(--orange); margin-bottom: 4px; }
  .price-note { font-weight: 700; }
</style>
</head>
<body>
<main class="spread">
  <section class="facts-panel">
    <h1 class="facts-title">Facts about LED displays</h1>

    <div class="fact-icon" style="left:40px;top:238px">
      <svg width="40" height="40" viewBox="0 0 44 44" fill="none" stroke="#fff" stroke-width="3" stroke-linecap="round" stroke-linejoin="round">
        <path d="M22 22 L22 6 M17 11 L22 6 L27 11"/>
        <path d="M22 22 L36 16 M30 12 L36 16 L32 22"/>
        <path d="M22 22 L34 36 M28 36 L34 36 L34 30"/>
        <path d="M22 22 L10 34 M10 28 L10 34 L16 34"/>
        <path d="M22 22 L6 18 M11 13 L6 18 L11 22"/>
      </svg>
    </div>
    <p class="fact-text" style="left:127px;top:237px;width:180px">LEDs can be used to draw people into your business, list product features, play in-store advertisements, deliver news about your organization…<strong>the possibilities are endless</strong>. It’s this flexibility that drives their popularity, and why these types of signs aren’t going away any time soon.</p>

    <div class="fact-icon" style="left:40px;top:401px">
      <svg width="42" height="42" viewBox="0 0 46 46" fill="none" stroke="#fff" stroke-width="3" stroke-linecap="round">
        <circle cx="20" cy="24" r="15"/><circle cx="20" cy="24" r="9"/><circle cx="20" cy="24" r="3" fill="#fff"/>
        <path d="M20 24 L42 24 M36 19 L42 24 L36 29"/>
      </svg>
    </div>
    <p class="fact-text" style="left:127px;top:400px;width:180px">More than half—60%, in fact—of buying decisions are made at the point of sale. LED signage displaying essential benefits and product information helps seal the deal with those still on the fence…all in a way that’s <strong>more effective and engaging than traditional sales methods.</strong></p>

    <div class="fact-icon" style="left:40px;top:614px">
      <svg width="40" height="40" viewBox="0 0 44 44" fill="none" stroke="#fff" stroke-width="3.2">
        <circle cx="22" cy="22" r="17"/><circle cx="22" cy="22" r="12"/>
        <path d="M26 16 C24 14 18 14 18 18 C18 22 26 21 26 26 C26 30 19 30 17 28 M22 12 L22 32" stroke-linecap="round"/>
      </svg>
    </div>
    <p class="fact-text" style="left:127px;top:570px;width:182px">The National Merchant Trade Bureau says that “Signs are <strong>the most effective, yet least expensive</strong>, form of advertising for the small business.” And that’s because small business owners using displays often see an increase in business between 15 and 150%. No other form of advertisement—from newspapers to radio to the Internet—offers the potential ROI of a solid LED sign.</p>

    <div class="fact-icon" style="left:388px;top:238px">
      <svg width="40" height="40" viewBox="0 0 44 44" fill="#fff" stroke="#fff" stroke-width="3" stroke-linecap="round" stroke-linejoin="round">
        <rect x="8" y="28" width="5" height="10" stroke="none"/>
        <rect x="16" y="24" width="5" height="14" stroke="none"/>
        <rect x="24" y="27" width="5" height="11" stroke="none"/>
        <rect x="32" y="18" width="5" height="20" stroke="none"/>
        <path d="M6 24 L16 14 L24 20 L36 8" fill="none"/>
        <path d="M29 8 L36 8 L36 15" fill="none"/>
      </svg>
    </div>
    <p class="fact-text" style="left:474px;top:234px;width:190px">LED displays ratchet up <strong>sales volume by more than 30%</strong>. LEDs streamline the shopping experience, from storefront to checkout. Companies using digital signs both within and outside their business report increased sales volume due to relief of frustration and more efficient up-sells and cross-sells.</p>

    <div class="fact-icon" style="left:388px;top:390px">
      <svg width="44" height="44" viewBox="0 0 48 48" fill="none" stroke="#fff" stroke-width="3.2">
        <path d="M4 24 C12 12 36 12 44 24 C36 36 12 36 4 24 Z"/>
        <circle cx="24" cy="24" r="7" fill="#fff"/>
      </svg>
    </div>
    <p class="fact-text" style="left:474px;top:390px;width:190px">A UK study found that almost <strong>90% of retailers considered LED signs essential for increasing their brand’s awareness in-store.</strong> LED displays can be updated effortlessly, allowing for seamless message customization. Unlike traditional in-store displays, which customers tend to “tune out” after repeated exposure, LEDs are quickly becoming the face of many stores and businesses.</p>

    <div class="fact-photo" role="img" aria-label="Photo of a restaurant storefront with a newly installed illuminated sign and an installer on a lift"></div>
  </section>

  <section class="clients-panel">
    <h2 class="clients-heading">We supply LED signs to many<br>Philadelphia area businesses.</h2>
    <p>Here’s what our clients like about them:</p>
    <p>They don’t dim when incandescent or fluorescent lights dim, it’s because their bulbs are filled with gasses that are prone to leaking after a period of wear and tear. Those leaks are what cause a reduction in brightness. LED bulbs don’t contain gas, and therefore, they don’t dim!</p>
    <p>&nbsp;They save power, and by saving you power, they’re saving you money, and you’re also saving the environment. While a typical neon light uses about 20 watts of power per foot, an LED will only use a little over 1 watt. Let’s put those numbers to work. Say you need to run 100 feet of light. LEDs will cost about 120 watts of power. If you crunch the same numbers against neon, you’ll be in for 2000 watts of power. If you light your sign for 10 hours per day, 365 days a year, that will add up to 438 annual kilowatt hours for the LED, and 7300 kilowatt hours for the neon. At a cost of $.012/kilowatt hour (which is the national average), your annual spend will be:</p>
    <div class="price-line price-neon">$876 for the neon sign</div>
    <div class="price-line price-led">$53 for the LED sign</div>
    <p class="price-note">That’s a 94% price difference.<br>LEDs are unrestrictive</p>
    <p>In other words, the ways in which they can be used are virtually limitless. Between color and movement options, what your sign can depict is only restricted by how creative you are. Your options are limitless with LED’s<br>Change your message and make it move</p>
    <p>You can update what your message says, and make it physically move or scroll with an LED sign. With a neon sign, the message is what it is. If you need to adjust what your LED says, you can do so. You can also display real-time information, such as the time or temperature. Changing your LED sign’s message is easy because you’ll make that happen via computer software.</p>
    <p>&nbsp;With an LED sign, your message will shine brighter against the signs of your competitors, and for cheaper and longer. So, do you need an LED sign for your Bucks County, PA business? Get in touch today and we’ll make one for you!</p>
  </section>
</main>
</body>
</html>
```